New Business card design to reflect rebrand

I would like a business card design with a good base colour for our new logo and also a placeholder for a profile pic of the card holder. the design needs to be editable to the point that we can easily change the picture of the person and use that design for printmoor etc. we are looking at a metalic finish business card so will need a good base colour to bring out the finish.

Target Market(s)

prospective customers

Industry/Entity Type

Business

Contact Information for Business Card

I would like one editable design that we can change the name of the card holder and profile picture. The design need to be in a format that be send to printmoor etc.

Our address is Fenwick Lodge, Mill Lane, Ashcombe Green, RG41 3TQ Tel no. 01632 960417

Requirements
Must have
• place holder for a profile pic for the card holder. in AI or preferably PSD format

```html
<!DOCTYPE html>
<html lang="en">
<head>
<meta charset="utf-8">
<title>Kestrow Workplace Services – Business Card</title>
<link rel="stylesheet" href="https://fonts.googleapis.com/css2?family=Open+Sans:wght@400;600;700&display=swap">
<style>
  :root {
    --navy: #3c4d69;
    --orange: #ee6b1c;
    --text-grey: #6b6b6b;
    --card-white: #ffffff;
    --card-shade: #ececec;
    --photo-grey: #a9a9a9;
    --photo-light: #d6d6d6;
    --backdrop: #e4e1dc;
  }
  * { box-sizing: border-box; margin: 0; padding: 0; }
  html, body {
    width: 1200px; height: 843px; overflow: hidden;
    background: var(--backdrop);
    font-family: "Open Sans", Arial, sans-serif;
  }
  .stage {
    width: 1200px; height: 843px;
    display: flex; align-items: center; justify-content: center; gap: 40px;
  }
  .card {
    position: relative;
    width: 540px; height: 309px;
    background: linear-gradient(135deg, var(--card-white) 55%, var(--card-shade) 100%);
    box-shadow: 0 6px 18px rgba(0,0,0,0.18);
    overflow: hidden;
  }
  .brand-name {
    color: var(--navy);
    font-weight: 700;
    letter-spacing: 0.04em;
    text-transform: uppercase;
    line-height: 1.05;
  }
  .brand-name .brand-word { display: block; font-size: 40px; }
  .brand-name .brand-tag { display: block; font-size: 15px; letter-spacing: 0.18em; }

  /* back of card */
  .card-back .brand-name { position: absolute; top: 26px; right: 30px; text-align: right; }
  .card-back .profile-photo {
    position: absolute; left: 0; bottom: 56px;
    width: 330px; height: 170px;
    background: linear-gradient(180deg, var(--photo-light) 0%, var(--photo-grey) 100%);
  }
  .card-back .web-band {
    position: absolute; left: 0; right: 0; bottom: 0;
    height: 56px; background: var(--orange);
    display: flex; align-items: center; padding-left: 28px;
  }
  .card-back .web-address {
    color: var(--card-white); font-size: 14px; letter-spacing: 0.22em;
  }

  /* front of card */
  .card-front .brand-name { position: absolute; top: 38px; left: 70px; }
  .card-front .address {
    position: absolute; top: 150px; left: 70px;
    color: var(--text-grey); font-size: 14px; line-height: 1.4;
    font-style: normal;
  }
  .card-front .phone {
    display: flex; align-items: center; gap: 8px; margin-top: 6px;
  }
  .card-front .phone svg { width: 12px; height: 12px; }
  .card-front .holder {
    position: absolute; right: 44px; bottom: 36px; text-align: right;
  }
  .card-front .holder-name {
    color: var(--navy); font-weight: 700; font-size: 18px; letter-spacing: 0.02em;
  }
  .card-front .holder-role {
    color: var(--orange); font-size: 14px; font-weight: 600;
  }
  .card-front .edge-tab {
    position: absolute; right: 0; bottom: 36px;
    width: 12px; height: 36px; background: var(--navy);
  }
</style>
</head>
<body>
<main class="stage">
  <section class="card card-back">
    <div class="brand-name">
      <span class="brand-word">Kestrow</span>
      <span class="brand-tag">Workplace Services</span>
    </div>
    <div class="profile-photo" role="img" aria-label="Profile photo of the card holder in soft grey tones"></div>
    <div class="web-band">
      <span class="web-address">www.kestrow.com</span>
    </div>
  </section>

  <section class="card card-front">
    <div class="brand-name">
      <span class="brand-word">Kestrow</span>
      <span class="brand-tag">Workplace Services</span>
    </div>
    <address class="address">
      Fenwick Lodge<br>
      Mill Lane, Ashcombe Green<br>
      RG41 3TQ
      <span class="phone">
        <svg viewBox="0 0 24 24" aria-hidden="true"><path fill="#ee6b1c" d="M6.6 10.8a15.1 15.1 0 0 0 6.6 6.6l2.2-2.2a1 1 0 0 1 1-.25 11.4 11.4 0 0 0 3.6.57 1 1 0 0 1 1 1V20a1 1 0 0 1-1 1A17 17 0 0 1 3 4a1 1 0 0 1 1-1h3.5a1 1 0 0 1 1 1c0 1.25.2 2.45.57 3.57a1 1 0 0 1-.25 1z"/></svg>
        01632 960417
      </span>
    </address>
    <div class="holder">
      <div class="holder-name">Daniel Hurst</div>
      <div class="holder-role">CEO/Founder</div>
    </div>
    <div class="edge-tab"></div>
  </section>
</main>
</body>
</html>
```